Thornwell Deli Needs a Web Page!

Thornwell Deli is a gourmet sandwich shop in Baltimore, MD USA.
We are due to open in about a month or so and we need a great web page that looks cool and is easy to use. Our Concept supports local farmers, ranchers, fishmongers & purveyors. All of our menu items are made from scratch using fresh local ingredients.

Target Market(s)

Urban people on the go & Anyone who is hungry and likes a great sandwich

Industry/Entity Type

Shop

Requirements
Must have
• We must have these 8 tabs:
Home
Menus
Gallery
About Us
Media & Events
Hours & Location
Order Online
Contact Us

Also we would like our Logo to be a focal point
Our Color scheme is Red, Black, Grey, White and a reddish-orange
however any and all colors are great and will be considered
We would love an area on the page for our own food photos to be added.
Nice to have
• Baltimore Skyline
Order Online Now Button
Free Wi-Fi Symbol
Dine-In, Take Out, Delivery,
Business Lunches, Tail Gate Platters, Catering
Should not have
• No Stock images of food or chefs.
(We want to put all of our own food photos up later.)
No Pink.

```html
<!DOCTYPE html>
<html lang="en">
<head>
<meta charset="utf-8">
<title>Thornwell Deli — Gourmet Sandwich Shop</title>
<link rel="stylesheet" href="https://fonts.googleapis.com/css2?family=Lobster&family=Open+Sans:wght@400&display=swap">
<style>
  :root {
    --bar-top: #6b6b6b;
    --bar-mid: #2a2a2a;
    --bar-bottom: #111111;
    --nav-text: #ffffff;
    --accent-red: #d8374f;
    --deep-red: #7a1424;
    --ink: #1a1a1a;
    --body-text: #555555;
    --heading-text: #4a4a4a;
    --panel-border: #d9d9d9;
    --page-bg: #ffffff;
    --footer-bg: #0d0d0d;
    --footer-text: #d6d6d6;
    --photo-dark: #2b1d14;
    --photo-warm: #7a4a2a;
    --photo-light: #e9c9a0;
  }
  * { margin: 0; padding: 0; box-sizing: border-box; }
  html, body { width: 1200px; height: 700px; overflow: hidden; background: var(--page-bg); }
  body { position: relative; font-family: "Open Sans", Verdana, sans-serif; }

  .top-nav {
    position: absolute; left: 0; top: 0; width: 1200px; height: 50px;
    background: linear-gradient(var(--bar-top), var(--bar-mid) 55%, var(--bar-bottom));
  }
  .top-nav a, .footer-nav a {
    position: absolute; transform: translateX(-50%); white-space: nowrap;
    font-family: "Lobster", cursive; color: var(--nav-text); text-decoration: none;
  }
  .top-nav a { top: 13px; font-size: 16px; }
  .top-nav a.is-current, .footer-nav a.is-current { color: var(--accent-red); }

  .brand {
    position: absolute; left: 0; top: 98px; width: 1200px;
    display: flex; justify-content: center; align-items: center; gap: 12px;
  }
  .brand-dot { width: 34px; height: 34px; border-radius: 50%; background: var(--accent-red); }
  .brand-name { font-family: "Lobster", cursive; font-size: 36px; color: var(--ink); line-height: 1; }

  .content-panel {
    position: absolute; left: 156px; top: 187px; width: 900px; height: 419px;
    border: 1px solid var(--panel-border); border-radius: 3px;
    box-shadow: 0 0 5px rgba(0,0,0,.15); background: var(--page-bg);
  }
  .feature-photo {
    position: absolute; left: 15px; top: 17px; width: 433px; height: 312px;
    padding: 4px; background: #fff; box-shadow: 0 0 6px rgba(0,0,0,.25); border-radius: 3px;
  }
  .feature-photo .photo-fill {
    width: 100%; height: 100%;
    background: radial-gradient(circle at 82% 22%, var(--photo-light), transparent 32%),
                radial-gradient(ellipse at 45% 55%, #cfd0d3 0 28%, transparent 48%),
                linear-gradient(135deg, var(--photo-dark), var(--photo-warm) 60%, var(--photo-dark));
  }
  .thumb-strip {
    position: absolute; left: 15px; top: 344px; width: 435px; height: 60px;
    background: #fff; border-radius: 6px; box-shadow: 0 0 6px rgba(0,0,0,.2);
  }
  .thumb-strip .arrow { position: absolute; top: 20px; font-size: 14px; color: #aaa; }
  .thumb-strip .arrow.prev { left: 10px; }
  .thumb-strip .arrow.next { right: 12px; }
  .thumb {
    position: absolute; top: 7px; width: 66px; height: 45px; padding: 2px;
    background: #fff; border: 1px solid #ddd;
  }
  .thumb span { display: block; width: 100%; height: 100%; background: linear-gradient(135deg, var(--photo-dark), var(--photo-warm)); }
  .thumb:nth-of-type(3) span { background: linear-gradient(135deg, #8a6a55, #e4dcd2); }
  .thumb:nth-of-type(4) span { background: linear-gradient(135deg, #e9c9a0, #6b4a35); }
  .thumb:nth-of-type(5) span { background: linear-gradient(135deg, #5a4a3e, #c9b9a8); }

  .welcome { position: absolute; left: 481px; top: 18px; width: 378px; }
  .welcome h1 { font-family: "Lobster", cursive; font-weight: 400; font-size: 20px; color: var(--heading-text); margin-left: -3px; }
  .welcome p {
    margin-top: 4px; font-size: 14.5px; line-height: 31px; color: var(--body-text); text-align: justify;
  }
  .welcome .lead { font-style: italic; text-decoration: underline; color: #333; }

  .badges { position: absolute; left: 610px; top: 350px; display: flex; gap: 28px; align-items: center; }
  .order-button {
    width: 70px; height: 40px; border-radius: 20px; background: var(--deep-red);
    border: 2px solid #ccc; box-shadow: 0 0 3px rgba(0,0,0,.4);
    display: flex; align-items: center; justify-content: center;
    font-family: "Lobster", cursive; font-size: 11px; color: #fff; line-height: 1; text-align: center;
  }

  .site-footer { position: absolute; left: 0; top: 629px; width: 1200px; height: 71px; background: var(--footer-bg); }
  .footer-nav a { top: 19px; font-size: 13px; color: var(--footer-text); }
  .copyright {
    position: absolute; left: 0; top: 44px; width: 1200px; text-align: center;
    font-family: "Lobster", cursive; font-size: 10px; color: var(--footer-text);
  }
  .copyright span { text-decoration: underline; }
</style>
</head>
<body>
  <nav class="top-nav">
    <a class="is-current" style="left:199px">Home</a>
    <a style="left:308px">Gallery</a>
    <a style="left:412px">About</a>
    <a style="left:545px">Media &amp; Events</a>
    <a style="left:707px">Hours &amp; Location</a>
    <a style="left:856px">Order Online</a>
    <a style="left:985px">Contact Us</a>
  </nav>

  <header class="brand">
    <span class="brand-dot"></span>
    <span class="brand-name">Thornwell Deli</span>
  </header>

  <main class="content-panel">
    <div class="feature-photo">
      <div class="photo-fill" role="img" aria-label="Featured food photo: sandwich plated on a white dish"></div>
    </div>

    <div class="thumb-strip">
      <span class="arrow prev">‹</span>
      <div class="thumb" style="left:28px"><span role="img" aria-label="Food photo thumbnail"></span></div>
      <div class="thumb" style="left:106px"><span role="img" aria-label="Food photo thumbnail"></span></div>
      <div class="thumb" style="left:184px"><span role="img" aria-label="Food photo thumbnail"></span></div>
      <div class="thumb" style="left:263px"><span role="img" aria-label="Food photo thumbnail"></span></div>
      <div class="thumb" style="left:340px"><span role="img" aria-label="Food photo thumbnail"></span></div>
      <span class="arrow next">›</span>
    </div>

    <section class="welcome">
      <h1>Welcome to our site</h1>
      <p><span class="lead">Thornwell Deli is a gourmet sandwich shop in Baltimore, MD USA.</span>
      We are due to open in about a month or so and we need a great web page that looks cool and is easy to use. Our Concept supports local farmers, ranchers, fishmongers &amp; purveyors. All of our menu items are made from scratch using fresh local ingredients. We are due to open in about a month or so and we need a great web page that looks cool and is easy to use.</p>
    </section>

    <div class="badges">
      <svg class="wifi-icon" width="60" height="44" viewBox="0 0 60 44" role="img" aria-label="Free Wi-Fi">
        <ellipse cx="30" cy="22" rx="29" ry="21" fill="#111"/>
        <g fill="none" stroke="#fff" stroke-width="3" stroke-linecap="round">
          <path d="M16 20 a20 20 0 0 1 28 0"/>
          <path d="M21 25 a13 13 0 0 1 18 0"/>
        </g>
        <circle cx="30" cy="31" r="3" fill="#fff"/>
      </svg>
      <div class="order-button">Order<br>Online Now</div>
    </div>
  </main>

  <footer class="site-footer">
    <nav class="footer-nav">
      <a class="is-current" style="left:375px">Home</a>
      <a style="left:435px">Gallery</a>
      <a style="left:497px">About</a>
      <a style="left:580px">Media &amp; Events</a>
      <a style="left:691px">Hours &amp; Location</a>
      <a style="left:796px">Order Online</a>
      <a style="left:884px">Contact Us</a>
    </nav>
    <p class="copyright">Copyright©2012, <span>Thornwell Deli</span></p>
  </footer>
</body>
</html>
```